INCREASED BUDGET -- Cover Art Template Needed For Record Label

We are an electronic music record label that needs a cover art template for our 2017 releases. The design must be easy to update in Photoshop with different text, colors, or patterns.

The winner will also be asked to design our social media banners for Facebook, Twitter, and SoundCloud, so there's an opportunity to make more money.

Words to describe our sound: sophisticated, forward-thinking, futuristic, modern, emotional

Please make the HA logo the focal point of your design. Feel free to modify our logo as needed. Bonus points for anyone that can find a way to visually represent the word "Harborline". Examples of artwork that we found attractive are included to provide inspiration.

You can view our previous releases by clicking on any of the links: https://www.trackvendor-example.com/label/harborline-audio/52741/releases

Target Market(s)

Electronic music lovers

Industry/Entity Type

Music Download

Font styles to use
Serif
Decorative
Other font styles liked:
• Aller Display, Aller Light

Requirements
Must have
• Harborline Audio record logo
• Name of artist: Owen Tarsley
• Title: Daybreak / Stay Close (Remixes)
Nice to have
• Tracklist:
• Stay Close (Brannok Remix)
• Daybreak (Velktone Remix)
• Catalog number: 382

```html
<!DOCTYPE html>
<html lang="en">
<head>
<meta charset="utf-8">
<title>Harborline Audio – Daybreak cover template</title>
<link rel="stylesheet" href="https://fonts.googleapis.com/css2?family=Amatic+SC:wght@400;700&family=PT+Sans+Narrow:wght@700&display=swap">
<style>
  :root {
    --canvas-gap: #f7ecee;
    --night-ink: #06050c;
    --swirl-purple: #2a1448;
    --swirl-blue: #141a4a;
    --text-white: #ffffff;
    --accent-gold: #f3ee3c;
    --glow-gold: rgba(150, 120, 40, 0.55);
    --accent-cyan: #19e6f2;
    --glow-cyan: rgba(20, 140, 190, 0.6);
    --font-title: "Amatic SC", "Arial Narrow", sans-serif;
    --font-label: "PT Sans Narrow", "Arial Narrow", sans-serif;
  }
  * { margin: 0; padding: 0; box-sizing: border-box; }
  html, body {
    width: 1200px;
    height: 594px;
    overflow: hidden;
    background: var(--canvas-gap);
  }
  .template-sheet {
    display: flex;
    justify-content: space-between;
    width: 1200px;
    height: 594px;
  }
  .cover {
    width: 594px;
    height: 594px;
    display: block;
  }
  .cover--gold { --accent: var(--accent-gold); --glow: var(--glow-gold); --artist: var(--accent-gold); }
  .cover--cyan { --accent: var(--accent-cyan); --glow: var(--glow-cyan); --artist: var(--text-white); }

  .release-title {
    font-family: var(--font-title);
    font-weight: 400;
    font-size: 34px;
    letter-spacing: 0.28em;
  }
  .release-title .title-lead { fill: var(--text-white); }
  .release-title .title-tail { fill: var(--accent); }

  .label-name {
    font-family: var(--font-label);
    font-weight: 700;
    font-size: 56px;
    fill: var(--accent);
    letter-spacing: 0.02em;
  }
  .label-url {
    font-family: var(--font-label);
    font-weight: 700;
    font-size: 17px;
  }
  .label-url .url-main { fill: var(--text-white); }
  .label-url .url-end { fill: var(--accent); }

  .artist-name {
    font-family: var(--font-title);
    font-weight: 700;
    font-size: 22px;
    letter-spacing: 0.62em;
    fill: var(--artist);
  }
</style>
</head>
<body>
<main class="template-sheet">

  <svg class="cover cover--gold" viewBox="0 0 594 594" aria-label="Daybreak cover, gold variant">
    <defs>
      <radialGradient id="swirl-gold" cx="50%" cy="50%" r="75%">
        <stop offset="0%" stop-color="var(--swirl-purple)"/>
        <stop offset="55%" stop-color="var(--swirl-blue)"/>
        <stop offset="100%" stop-color="var(--night-ink)"/>
      </radialGradient>
      <radialGradient id="halo-gold" cx="50%" cy="50%" r="50%">
        <stop offset="0%" stop-color="var(--glow)"/>
        <stop offset="80%" stop-color="var(--glow)" stop-opacity="0.7"/>
        <stop offset="100%" stop-color="var(--glow)" stop-opacity="0"/>
      </radialGradient>
      <path id="arc-gold" d="M 338 152 Q 478 138 542 252"/>
    </defs>
    <rect class="swirl-field" width="594" height="594" fill="url(#swirl-gold)" role="img" aria-label="Flowing purple and blue line pattern on black"/>
    <ellipse class="logo-halo" cx="296" cy="316" rx="212" ry="112" fill="url(#halo-gold)"/>
    <text class="release-title"><textPath href="#arc-gold"><tspan class="title-lead">DAY</tspan><tspan class="title-tail">BREAK</tspan></textPath></text>
    <text class="label-name" x="296" y="290" text-anchor="middle">HARBORLINE</text>
    <text class="label-name" x="296" y="346" text-anchor="middle">AUDIO</text>
    <text class="label-url" x="296" y="400" text-anchor="middle"><tspan class="url-main">www.harborlineaudio</tspan><tspan class="url-end">.com</tspan></text>
    <text class="artist-name" x="300" y="522" text-anchor="middle">OWEN TARSLEY</text>
  </svg>

  <svg class="cover cover--cyan" viewBox="0 0 594 594" aria-label="Daybreak cover, cyan variant">
    <defs>
      <radialGradient id="swirl-cyan" cx="50%" cy="50%" r="75%">
        <stop offset="0%" stop-color="var(--swirl-purple)"/>
        <stop offset="55%" stop-color="var(--swirl-blue)"/>
        <stop offset="100%" stop-color="var(--night-ink)"/>
      </radialGradient>
      <radialGradient id="halo-cyan" cx="50%" cy="50%" r="50%">
        <stop offset="0%" stop-color="var(--glow)"/>
        <stop offset="80%" stop-color="var(--glow)" stop-opacity="0.7"/>
        <stop offset="100%" stop-color="var(--glow)" stop-opacity="0"/>
      </radialGradient>
      <path id="arc-cyan" d="M 338 152 Q 478 138 542 252"/>
    </defs>
    <rect class="swirl-field" width="594" height="594" fill="url(#swirl-cyan)" role="img" aria-label="Flowing purple and blue line pattern on black"/>
    <ellipse class="logo-halo" cx="296" cy="316" rx="212" ry="112" fill="url(#halo-cyan)"/>
    <text class="release-title"><textPath href="#arc-cyan"><tspan class="title-lead">DAY</tspan><tspan class="title-tail">BREAK</tspan></textPath></text>
    <text class="label-name" x="296" y="290" text-anchor="middle">HARBORLINE</text>
    <text class="label-name" x="296" y="346" text-anchor="middle">AUDIO</text>
    <text class="label-url" x="296" y="400" text-anchor="middle"><tspan class="url-main">www.harborlineaudio</tspan><tspan class="url-end">.com</tspan></text>
    <text class="artist-name" x="300" y="522" text-anchor="middle">OWEN TARSLEY</text>
  </svg>

</main>
</body>
</html>
```